Etiketten-Design für Nahrungsergänzungsmittel
Zielgruppe
Die Firma vertreibt Nahrungsergänzungsmittel, gesunde Lebensmittel, Lifestyle und Wellnessprodukte. Dies vor allem im Fitness und Sport Bereich. Die Marke und das entsprechende Logo sollen auf eine jüngere Zielgruppe 25+ ausgerichtet sein. Personen die für Ihren Körper und Gesundheit Sport treiben und zusätzlich Unterstützung benötigen. Die Produkte werden über Pictoloop durch eine Fitnesstrainerin beworben, und hauptsächlich über Varuno vertrieben. Produkte sind z. B. Produkte zur Ausdauersteigerung, verbesserte Konzentration, Schlaf, Stressbewältigung. Protein Shakes oder Vitamine für Veganer. No gos, Diät Produkte 5kg in 3 Tagen, Potenzsteigerung, Brustvergrößerung oder ähnliches.
Aufgabenstellung
Das Etikett wird auf einen wiederverschließbaren schwarz matten Kraftpapier Beutel im Format 28x20cm aufgebracht. Der Beutel und auch das Etikett sind kompostierbar, sieht aber beides hochwertig aus. Das Produkt ist ein veganes Proteinpulver zum anrühren mit Wasser oder Milchalternative. Einen ersten Entwurf habe ich hochgeladen.

```html
<!DOCTYPE html>
<html lang="de">
<head>
<meta charset="utf-8">
<title>LIORA Veganer Protein Shake – Etikett</title>
<link href="https://fonts.googleapis.com/css2?family=Arimo:wght@400;700&family=Roboto+Condensed:wght@400;700&family=Oswald:wght@300;400&family=Orbitron:wght@700;900&family=Yellowtail&display=swap" rel="stylesheet">
<style>
  :root {
    --ink: #0b0b0c;
    --panel: #1c1c1e;
    --teal: #1fa89b;
    --teal-dark: #137a71;
    --white: #ffffff;
    --row-light: #9d9fa1;
    --row-dark: #7f8183;
    --row-line: #5a5c5e;
  }
  * { margin: 0; padding: 0; box-sizing: border-box; }
  html, body { width: 1200px; height: 834px; overflow: hidden; background: var(--ink); }
  .label {
    position: relative; width: 1200px; height: 834px; overflow: hidden;
    background: radial-gradient(ellipse at 55% 45%, #161617 0%, var(--ink) 70%);
    font-family: "Arimo", Arial, sans-serif; color: var(--white);
  }
  .abs { position: absolute; }

  .hex-field {
    left: 222px; top: 0; width: 800px; height: 265px;
    background: radial-gradient(ellipse at 50% 30%, #2a2b2d 0%, #1a1b1c 55%, rgba(11,11,12,0) 100%);
  }
  .hex-field.bottom-left { left: 280px; top: 622px; width: 170px; height: 190px;
    background: linear-gradient(180deg, #252628 0%, #1b1c1d 100%); }
  .hex-field.bottom-right { left: 760px; top: 715px; width: 110px; height: 95px;
    background: linear-gradient(180deg, #242527 0%, #1b1c1d 100%); }

  .product-type { left: 28px; top: 148px; font-size: 14.5px; line-height: 17px; }
  .ingredients { left: 28px; top: 218px; font-size: 11.5px; line-height: 13.5px; }

  table { border-collapse: collapse; font-family: "Roboto Condensed", Arial Narrow, sans-serif; font-size: 10px; color: var(--white); }
  td, th { border: 1px solid var(--row-line); padding: 1px 3px; }
  th { background: var(--teal); font-weight: 700; text-align: left; font-size: 10px; height: 16px; }
  tbody tr:nth-child(odd) td { background: var(--row-light); }
  tbody tr:nth-child(even) td { background: var(--row-dark); }
  .num { text-align: right; }
  .nutrition { left: 25px; top: 280px; width: 330px; }
  .nutrition td { height: 17px; }
  .nutrition .tall td { height: 26px; vertical-align: top; line-height: 10px; }
  .amino { left: 25px; top: 459px; width: 330px; }
  .amino td { height: 18px; }

  .brand-small { left: 30px; top: 672px; font-family: "Orbitron", sans-serif; font-weight: 900; font-size: 21px; letter-spacing: 1px; }
  .usage { left: 26px; top: 716px; font-size: 12px; line-height: 13.7px; }

  .brand-main { left: 391px; top: 326px; width: 400px; text-align: center; font-family: "Orbitron", sans-serif; font-weight: 900; font-size: 54px; letter-spacing: 2px; }
  .product-name { left: 380px; top: 440px; width: 420px; text-align: center; font-family: "Orbitron", sans-serif; font-weight: 900; line-height: 48px; }
  .product-name .teal { color: var(--teal); font-size: 42px; letter-spacing: 2px; display: block; }
  .product-name .white { color: var(--white); font-size: 40px; letter-spacing: 12px; display: block; }

  .benefits { left: 418px; top: 654px; display: flex; align-items: center; gap: 10px;
    font-family: "Oswald", sans-serif; font-weight: 300; font-size: 11px; line-height: 13px; letter-spacing: .3px; }
  .benefit { display: flex; align-items: center; gap: 8px; }
  .divider { width: 1px; height: 30px; background: var(--white); }

  .servings { left: 510px; top: 715px; width: 193px; height: 37px; border-radius: 19px; background: var(--teal);
    font-family: "Orbitron", sans-serif; font-weight: 900; font-size: 17px; color: var(--ink); display: flex; align-items: center; justify-content: center; letter-spacing: 1px; }

  .photo { left: 820px; top: 222px; width: 288px; height: 480px;
    background: linear-gradient(180deg, #c9a27f 0%, #6b7e98 45%, #2a2b2e 75%, #0f4d48 100%);
    clip-path: polygon(50% 0, 100% 30%, 100% 72%, 50% 100%, 0 72%, 0 30%); }

  .greeting { left: 990px; top: 675px; width: 175px; text-align: center; font-family: "Yellowtail", cursive; color: var(--teal); font-size: 11.5px; line-height: 16px; }
  .social { left: 1010px; top: 708px; display: flex; align-items: center; gap: 6px; font-size: 13px; }
  .social .square { width: 12px; height: 12px; border: 1.5px solid var(--teal); border-radius: 3px; }

  .address { left: 877px; top: 739px; font-size: 11px; line-height: 13px; }
  .contents { left: 1005px; top: 739px; font-size: 11px; line-height: 13px; }

  .band { left: 0; top: 808px; width: 1200px; height: 26px; background: var(--teal); }
  .net-weight { left: 400px; top: 786px; width: 390px; height: 48px; }
  .net-weight span { position: absolute; left: 0; top: 12px; width: 100%; text-align: center;
    font-family: "Orbitron", sans-serif; font-weight: 900; color: var(--teal); font-size: 18px; letter-spacing: 1px; }
</style>
</head>
<body>
<main class="label">
  <div class="abs hex-field" role="img" aria-label="Dunkles Wabenmuster aus Sechsecken mit türkisen Kanten"></div>
  <div class="abs hex-field bottom-left" role="img" aria-label="Dunkle Sechseck-Waben"></div>
  <div class="abs hex-field bottom-right" role="img" aria-label="Dunkle Sechseck-Waben"></div>

  <p class="abs product-type">Getränkepulver zur Herstellung eines<br>veganen Eiweißgetränkes mit Süßungsmittel -<br>Geschmacksrichtung Vanille</p>
  <p class="abs ingredients">Zutaten:&nbsp; Eiweißmischung (93%) (Erbseneiweiß, Reiseiweiß,<br>Hanfsamenpulver, Bio Kürbiskerneiweiß), Aroma,<br>Verdickungsmittel: Xanthan, Kokosnussmilchpulver,<br>Süßungsmittel: Sucralose</p>

  <table class="abs nutrition">
    <thead><tr><th style="width:44%">Nährwertangaben pro</th><th class="num" style="width:26%">100g</th><th class="num">Portion = 30g</th></tr></thead>
    <tbody>
      <tr class="tall"><td>Energie</td><td class="num">1.694 kJ /<br>401 kcal</td><td class="num">508 kJ /<br>120 kcal</td></tr>
      <tr><td>Fett</td><td class="num">8,3 g</td><td class="num">2,5 g</td></tr>
      <tr><td>- davon gesättigte Fettsäuren</td><td class="num">2,2 g</td><td class="num">0,7 g</td></tr>
      <tr><td>Kohlenhydrate</td><td class="num">4,0 g</td><td class="num">1,2 g</td></tr>
      <tr><td>- davon Zucker</td><td class="num">1,2 g</td><td class="num">0,4 g</td></tr>
      <tr><td>Ballaststoffe</td><td class="num">4,4 g</td><td class="num">1,3 g</td></tr>
      <tr><td>Eiweiß</td><td class="num">75,3 g</td><td class="num">22,6 g</td></tr>
      <tr><td>Salz</td><td class="num">2,15 g</td><td class="num">0,64 g</td></tr>
    </tbody>
  </table>

  <table class="abs amino">
    <thead><tr><th colspan="6">Aminosäurenprofil pro 100g Eiweiß</th></tr></thead>
    <tbody>
      <tr><td>Isoleucin</td><td class="num">4,4 g</td><td>Tryptophan</td><td class="num">1,1 g</td><td>Alanin</td><td class="num">8,9 g</td></tr>
      <tr><td>Leucin</td><td class="num">8,4 g</td><td>Valin</td><td class="num">5,3 g</td><td>Asparaginsäure</td><td class="num">11,1 g</td></tr>
      <tr><td>Lysin</td><td class="num">6,7 g</td><td>Histidin</td><td class="num">2,5 g</td><td>Glutaminsäure</td><td class="num">17,2 g</td></tr>
      <tr><td>Methionin</td><td class="num">1,4 g</td><td>Arginin</td><td class="num">8,9 g</td><td>Glycin</td><td class="num">4,2 g</td></tr>
      <tr><td>Phenylalanin</td><td class="num">5,5 g</td><td>Tyrosin</td><td class="num">3,8 g</td><td>Prolin</td><td class="num">4,4 g</td></tr>
      <tr><td>Threonin</td><td class="num">3,7 g</td><td>Cystein</td><td class="num">1,4 g</td><td>Serin</td><td class="num">5,1g</td></tr>
    </tbody>
  </table>

  <div class="abs brand-small">LIORA</div>
  <p class="abs usage">Verzehrempfehlung: 30 g Pulver<br>in 300 ml Wasser lösen;<br>Das Produkt ist kühl, trocken und<br>dunkel zu lagern.</p>

  <div class="abs brand-main">LIORA</div>
  <h1 class="abs product-name"><span class="teal">VEGANER</span><span class="teal">PROTEIN</span><span class="white">SHAKE</span></h1>

  <div class="abs benefits">
    <div class="benefit">
      <svg width="28" height="34" viewBox="0 0 28 34" fill="none" stroke="#1fa89b" stroke-width="1.6"><circle cx="14" cy="20" r="12"/><circle cx="14" cy="20" r="8.5"/><path d="M11 3h6M14 3v5M14 20l4-5"/></svg>
      <span>FAST WORKOUT<br>RECOVERY</span>
    </div>
    <div class="divider"></div>
    <div class="benefit">
      <svg width="24" height="34" viewBox="0 0 24 34" fill="none" stroke="#1fa89b" stroke-width="1.4"><path d="M4 2c2 8-3 14-1 30M20 2c-2 8 3 14 1 30M7 22l5 8 5-8"/></svg>
      <span>BETTER NUTRIENT<br>ABSORPTION DIGESTION</span>
    </div>
    <div class="divider"></div>
    <div class="benefit">
      <svg width="34" height="30" viewBox="0 0 34 30" fill="none" stroke="#1fa89b" stroke-width="1.6"><path d="M17 28C4 18 1 13 1 8a7.5 7.5 0 0 1 16-2 7.5 7.5 0 0 1 16 2c0 5-3 10-16 20z"/><path d="M3 15h9l2-4 3 8 2-4h12"/></svg>
      <span>SUPPORT HEALTHY<br>INSULIN LEVELS</span>
    </div>
  </div>

  <div class="abs servings">30 SERVINGS</div>

  <div class="abs photo" role="img" aria-label="Foto der Fitnesstrainerin mit verschränkten Armen in Sporttop und Leggings vor türkisem Rahmen"></div>

  <p class="abs greeting">Besucht uns auch auf Pictoloop<br>Liebe Grüße Liora</p>
  <div class="abs social"><span class="square"></span><span>liorabyliora</span></div>

  <p class="abs address">LIORA UG<br>Lindenhofweg 12<br>76199 Talbrunn<br>info@liorabyliora.de</p>
  <p class="abs contents">Inhalt: 600g Eiweißpulver für<br>20 Shakes<br>Mindestens haltbar bis Ende:<br>08/2023; Losnummer:977109</p>

  <div class="abs band"></div>
  <div class="abs net-weight">
    <svg width="390" height="48" viewBox="0 0 390 48"><polygon points="40,0 350,0 390,48 0,48" fill="#1fa89b"/><polygon points="42,3 348,3 386,48 4,48" fill="#1c1c1e"/></svg>
    <span>NET WT. 5 LBS</span>
  </div>
</main>
</body>
</html>
```